Orthodontic Liaison Guild Annual Conference 2016 Flyer

We need a two page attention grabbing flyer promoting our upcoming conference in Dallas, TX at the Brackenridge Inn on August 27th and 28th 2016. The flyer should give information about the conference and what you will learn by attending and to accept registration through an Ticketvale link. Our mission is to define, educate and support the role of the dental implant coordinator. Bringing together like-minded professionals to network, practice share and define our role in the delivery of comprehensive patient care. 2 day annual conference open to Surgical implant coordinators and their surgeons

Target Market(s)

Surgical Implant Treatment Coordinators, their surgeons, and surgical team members

Industry/Entity Type

Dental

Requirements
Must have
• The ability for me to make changes.
Nice to have
• professional, eye catching,

```html
<!DOCTYPE html>
<html lang="en">
<head>
<meta charset="utf-8">
<title>Orthodontic Liaison Guild Annual Conference 2016 Flyer</title>
<link rel="stylesheet" href="https://fonts.googleapis.com/css2?family=Roboto:wght@400;500;700&display=swap">
<style>
  :root {
    --backdrop: #a3a3a3;
    --paper: #ffffff;
    --blue-deep: #0b5cb5;
    --blue-bright: #23a6e6;
    --navy: #0a2d66;
    --text: #2b2b2b;
    --muted: #f1f2f4;
  }
  * { margin: 0; padding: 0; box-sizing: border-box; }
  html, body { width: 1200px; height: 896px; overflow: hidden; }
  body {
    background: var(--backdrop);
    font-family: "Roboto", Arial, sans-serif;
    color: var(--text);
    position: relative;
  }
  .page {
    position: absolute;
    top: 48px;
    width: 560px;
    height: 800px;
    background: var(--paper);
    overflow: hidden;
  }
  .page--cover { left: 40px; }
  .page--details { left: 600px; background: linear-gradient(90deg, #ffffff 55%, var(--muted)); }
  .page-art { position: absolute; inset: 0; width: 560px; height: 800px; }

  .brand {
    position: absolute; left: 40px; top: 44px;
    display: flex; align-items: center; gap: 8px;
    font-size: 14px; font-weight: 500; color: var(--blue-deep);
  }
  .brand-dot { width: 12px; height: 12px; border-radius: 50%; background: var(--blue-bright); }

  .cover-title { position: absolute; left: 38px; top: 128px; }
  .cover-year { font-size: 50px; font-weight: 700; color: var(--blue-deep); line-height: 1; }
  .cover-sub { margin-top: 10px; font-size: 19px; line-height: 26px; color: var(--blue-bright); }
  .cover-sub strong { font-weight: 500; }

  .contact-list { position: absolute; left: 38px; top: 455px; list-style: none; }
  .contact-item { display: flex; align-items: center; gap: 14px; height: 60px; font-size: 15px; color: #333; }
  .contact-icon {
    width: 46px; height: 46px; border-radius: 50%;
    background: var(--blue-bright);
    display: flex; align-items: center; justify-content: center; flex: none;
  }
  .contact-icon svg { width: 22px; height: 22px; }

  .details-list {
    position: absolute; left: 22px; top: 104px; width: 350px;
    list-style: none; font-size: 12.3px; line-height: 19px;
  }
  .details-list li { position: relative; padding-left: 10px; }
  .details-list li::before {
    content: ""; position: absolute; left: 0; top: 7px;
    width: 5px; height: 5px; border-radius: 50%; background: var(--blue-bright);
  }
  .details-meals {
    position: absolute; left: 28px; top: 640px;
    font-size: 15px; color: var(--blue-bright);
  }
  .details-booking {
    position: absolute; left: 28px; top: 664px; width: 524px;
    font-size: 10.8px; line-height: 17px; white-space: nowrap;
  }
  .details-booking a { color: var(--blue-bright); text-decoration: none; display: block; }
</style>
</head>
<body>

<section class="page page--cover">
  <svg class="page-art" viewBox="0 0 560 800">
    <defs>
      <linearGradient id="photoTone" x1="0" y1="0" x2="1" y2="0.6">
        <stop offset="0" stop-color="#eef2f8"/>
        <stop offset="0.55" stop-color="#dfe4ee"/>
        <stop offset="1" stop-color="#cfa978"/>
      </linearGradient>
    </defs>
    <polygon role="img" aria-label="Photo of a dental professional in safety glasses and mask at work"
             points="250,0 560,0 560,560 40,300" fill="url(#photoTone)"/>
    <polygon points="0,272 0,318 560,588 560,540" fill="var(--blue-bright)"/>
    <polygon points="0,318 0,362 560,632 560,588" fill="var(--blue-deep)"/>
    <polygon points="0,362 0,460 200,460" fill="var(--navy)"/>
    <polygon points="330,560 560,610 560,668" fill="var(--blue-deep)"/>
    <polygon points="0,696 260,760 0,760" fill="var(--blue-bright)"/>
    <polygon points="0,728 0,760 130,760" fill="var(--blue-deep)"/>
  </svg>

  <div class="brand"><span class="brand-dot"></span>Orthodontic Liaison Guild</div>

  <div class="cover-title">
    <div class="cover-year">2016</div>
    <p class="cover-sub"><strong>Orthodontic Liaison</strong><br>Guild OLG Conference</p>
  </div>

  <ul class="contact-list">
    <li class="contact-item">
      <span class="contact-icon"><svg viewBox="0 0 24 24" fill="none" stroke="#fff" stroke-width="2" stroke-linecap="round" stroke-linejoin="round"><path d="M5 3h4l2 5-2.5 1.5a11 11 0 0 0 6 6L16 13l5 2v4a2 2 0 0 1-2 2A16 16 0 0 1 3 5a2 2 0 0 1 2-2z"/></svg></span>
      214-555-0148
    </li>
    <li class="contact-item">
      <span class="contact-icon"><svg viewBox="0 0 24 24" fill="none" stroke="#fff" stroke-width="2" stroke-linejoin="round"><rect x="3" y="6" width="18" height="12"/><path d="M3 6l9 7 9-7"/></svg></span>
      info@olguild.org
    </li>
    <li class="contact-item">
      <span class="contact-icon"><svg viewBox="0 0 24 24" fill="none" stroke="#fff" stroke-width="1.8"><circle cx="12" cy="12" r="9"/><path d="M3 12h18M12 3c3 3 3 15 0 18M12 3c-3 3-3 15 0 18"/></svg></span>
      http://www.olguild.org
    </li>
    <li class="contact-item">
      <span class="contact-icon"><svg viewBox="0 0 24 24" fill="#fff"><path d="M12 2a7 7 0 0 0-7 7c0 5 7 13 7 13s7-8 7-13a7 7 0 0 0-7-7zm0 9.5A2.5 2.5 0 1 1 12 6.5a2.5 2.5 0 0 1 0 5z"/></svg></span>
      <span>Kastanienweg 12b<br>10437 Berlin</span>
    </li>
  </ul>
</section>

<section class="page page--details">
  <svg class="page-art" viewBox="0 0 560 800">
    <defs>
      <linearGradient id="collageTone" x1="0" y1="0" x2="1" y2="1">
        <stop offset="0" stop-color="#e6e6e6"/>
        <stop offset="1" stop-color="#9a9a9a"/>
      </linearGradient>
    </defs>
    <polygon points="0,28 100,28 0,110" fill="var(--blue-deep)"/>
    <polygon points="190,28 560,28 560,112" fill="var(--blue-bright)"/>
    <polygon points="330,28 560,28 560,72" fill="var(--blue-deep)"/>
    <g role="img" aria-label="Diamond collage of greyscale clinical photos" fill="url(#collageTone)">
      <polygon points="490,270 550,330 490,390 430,330"/>
      <polygon points="440,392 500,452 440,512 380,452"/>
      <polygon points="560,396 560,508 504,452"/>
      <polygon points="500,512 560,572 500,632 440,572"/>
    </g>
    <polygon points="0,700 250,758 0,758" fill="var(--blue-bright)"/>
    <polygon points="0,728 0,758 130,758" fill="var(--blue-deep)"/>
    <polygon points="560,705 560,758 500,758" fill="var(--blue-deep)"/>
  </svg>

  <ul class="details-list">
    <li>-Saturday 8/27 and Sunday 8/28 at The Brackenridge Inn Dallas, TX</li>
    <li>-Conference open to Surgical Implant Treatment Coordinators and their surgeons</li>
    <li>-Cost by June 30th $699, after June 30th $769</li>
    <li>-OLG member cost $100 off conference registration</li>
    <li>-Multiple team member discount $75 off conference registration</li>
    <li>-2 day Annual Orthodontic Liaison Guild conference</li>
    <li>-Great speaker and topic lineup</li>
    <li>-Breakout sessions including internet marketing, financial, communication, and utilizing an SITC</li>
    <li>-Additional moderated Dr only breakout and SITC only breakout</li>
    <li>-Q&amp;A and practice sharing from a Surgeon/SITC panel with both OMS and Perio practices</li>
    <li>-Speakers – Dr. Marcus Ellery, DDS, MSD, Prosthodontist “Healthy Implants from Start to Finish”, Dana Whitcombe, America’s Body Language Expert and contributor to Brightwave Report, “The Body Language of Effective Communication”, Dr. Howard T. Lindell, DDS, Professor of Surgery &amp; Chief, Coastal State School of Medicine, Dept of OMS, “The Effective use of rhBMP in Implant Dentistry”, Renee Calder, Professional Speaker, Author and Conversation Coach, “Team Building, Communication, and Case Acceptance”</li>
  </ul>

  <p class="details-meals">Breakfast and Lunch included</p>
  <p class="details-booking">Book your hotel reservation at The Brackenridge Inn $169/night room block through August 4, 2016
    <a href="https://book.staylink-reserve.com/event?mode=welcome&amp;id=20160827">https://book.staylink-reserve.com/event?mode=welcome&amp;id=20160827</a>
  </p>
</section>

</body>
</html>
```